Use Existing Logo to Design Letterhead, Envelope and Presentation Folder

We are a storm shelter company based out of Oklahoma City. We have an existing logo and brand image. We are looking for professionally designed letterhead, mailing envelopes and folders using our brand guidelines (attached). The font to be used is Futura.

The image represents simple professionalism.
We compete on quality, not price.
We value attention to detail and craftsmanship in our work.
The colors and layout are bold and clean.

Again, this is for:
1) Letterhead - contains name, address, phone, fax, and website address
2) Envelopes - logo, tagline and return address
3) Presentation Folders - logo and tag line

Our tag line is:
"Heartland's Trusted Tornado-Tested Shelters and Home Safety Solutions"

Please submit your designs and once we have the initial layouts, we will provide the top designers with our contact information.

Good luck!

```html
<!DOCTYPE html>
<html lang="en">
<head>
<meta charset="utf-8">
<title>Keystone Shelters Stationery</title>
<link rel="stylesheet" href="https://fonts.googleapis.com/css2?family=Jost:wght@400;500;600&display=swap">
<style>
  :root {
    --brand-blue: #1f2c9c;
    --brand-grey: #8a8b8f;
    --ink: #3a3a3a;
    --paper: #f3f3f2;
    --backdrop: #e6e6e6;
    --band-grey: #8e8f93;
    --flap-line: #d6d6d4;
  }
  * { box-sizing: border-box; margin: 0; padding: 0; }
  html, body { width: 1200px; height: 900px; overflow: hidden; }
  body {
    background: var(--backdrop);
    font-family: "Jost", "Futura", sans-serif;
    color: var(--ink);
    position: relative;
  }
  address { font-style: normal; }
  .sheet { position: absolute; background: var(--paper); }

  /* Letterhead */
  .letterhead { left: 102px; top: 105px; width: 482px; height: 682px; }
  .letterhead .side-band { position: absolute; left: 0; top: 0; width: 38px; height: 100%; background: var(--brand-blue); }
  .letterhead .footer-band {
    position: absolute; left: 38px; right: 0; bottom: 0; height: 34px;
    background: var(--band-grey); color: #f2f2f2;
    font-size: 10px; letter-spacing: 0.3px; text-align: center; line-height: 34px;
    white-space: nowrap;
  }
  .brand-name {
    color: var(--brand-blue); font-weight: 500; text-transform: uppercase;
    display: flex; align-items: center; gap: 7px; line-height: 1; white-space: nowrap;
  }
  .brand-name .mark { width: 10px; height: 10px; background: var(--brand-blue); flex: none; }
  .letterhead .brand-name { position: absolute; left: 58px; top: 88px; font-size: 18px; letter-spacing: 1px; }
  .contact {
    position: absolute; right: 26px; top: 22px; text-align: right;
    font-size: 9px; line-height: 11.5px; font-weight: 500;
  }
  .contact .phones { margin-top: 14px; }
  .contact .label { color: var(--brand-blue); }
  .contact .web { margin-top: 18px; color: var(--brand-blue); font-size: 10px; font-weight: 600; }
  .letter-body {
    position: absolute; left: 84px; top: 175px; width: 351px;
    font-size: 9.9px; line-height: 11.6px; font-weight: 500; text-align: justify;
    letter-spacing: 0.1px;
  }
  .letter-body p { margin-bottom: 11.6px; }

  /* Envelope back */
  .envelope-back { left: 627px; top: 108px; width: 539px; height: 256px; }
  .envelope-back svg { position: absolute; left: 0; top: 0; }

  /* Envelope front */
  .envelope-front { left: 627px; top: 385px; width: 539px; height: 258px; }
  .envelope-front .brand-name { position: absolute; left: 16px; top: 18px; font-size: 22px; letter-spacing: 0.5px; }
  .return-address {
    position: absolute; left: 17px; top: 56px;
    font-size: 8px; line-height: 10px; font-weight: 600; color: var(--brand-blue);
  }
  .envelope-front .tagline {
    position: absolute; left: 104px; bottom: 9px;
    font-size: 7.6px; font-weight: 600; color: var(--brand-blue); white-space: nowrap;
  }

  /* Business cards */
  .card-back { left: 627px; top: 665px; width: 217px; height: 124px; overflow: hidden; }
  .card-back .storm-photo {
    width: 100%; height: 100%;
    background: linear-gradient(180deg, #d9d9d9 0%, #c7c7c7 55%, #b9b9b9 75%, #d2d2d2 100%);
  }
  .card-front { left: 869px; top: 665px; width: 217px; height: 124px; }
  .card-front .brand-name {
    position: absolute; left: 0; right: 0; top: 88px; justify-content: center;
    font-size: 13px; letter-spacing: 0.8px;
  }
</style>
</head>
<body>

<section class="sheet letterhead">
  <div class="side-band"></div>
  <div class="brand-name"><span class="mark"></span>Keystone Shelters</div>
  <address class="contact">
    <div>4820 West Harbor Avenue, Suite 200-B</div>
    <div>Oklahoma City, Oklahoma 73120</div>
    <div class="phones"><span class="label">P:</span> (405) 555-0142</div>
    <div><span class="label">F:</span> (405) 555-0187</div>
    <div class="web">www.keystoneshelters.com</div>
  </address>
  <div class="letter-body">
    <p>Dear Client,</p>
    <p>Lorem ipsum dolor sit amet, consectetur adipisicing elit, sed do eiusmod tempor incididunt ut labore et dolore magna aliqua. Ut enim ad minim veniam, quis nostrud exercitation ullamco laboris nisi ut aliquip ex ea commodo consequat.</p>
    <p>Duis aute irure dolor in reprehenderit in voluptate velit esse cillum dolore eu fugiat nulla pariatur. Excepteur sint occaecat cupidatat non proident, sunt in culpa qui officia deserunt mollit anim id est laborum. Sed ut perspiciatis unde omnis iste natus error sit voluptatem accusantium doloremque laudantium, totam rem aperiam, eaque ipsa quae ab illo inventore veritatis et quasi architecto beatae vitae dicta sunt explicabo.</p>
    <p>Nemo enim ipsam voluptatem quia voluptas sit aspernatur aut odit aut fugit, sed quia consequuntur magni dolores eos qui ratione voluptatem sequi nesciunt. Neque porro quisquam est, qui dolorem ipsum quia dolor sit amet, consectetur, adipisci velit, sed quia non numquam eius modi tempora incidunt ut labore et dolore magnam aliquam quaerat voluptatef.</p>
    <p>Respectfully,</p>
    <p>Yours</p>
  </div>
  <div class="footer-band">Heartland's Trusted Tornado-Tested Shelters and Home Safety Solutions</div>
</section>

<section class="sheet envelope-back">
  <svg width="539" height="256" viewBox="0 0 539 256" aria-hidden="true">
    <polyline points="4,0 12,89 527,89 535,0" fill="none" stroke="var(--flap-line)" stroke-width="1"/>
  </svg>
</section>

<section class="sheet envelope-front">
  <div class="brand-name">Keystone Shelters</div>
  <address class="return-address">
    <div>4820 West Harbor Avenue, Suite 200-B</div>
    <div>Oklahoma City, Oklahoma 73120</div>
  </address>
  <div class="tagline">Heartland's Trusted Tornado-Tested Shelters and Home Safety Solutions</div>
</section>

<section class="sheet card-back">
  <div class="storm-photo" role="img" aria-label="Grey photograph of a tornado over open plains"></div>
</section>

<section class="sheet card-front">
  <div class="brand-name"><span class="mark"></span>Keystone Shelters</div>
</section>

</body>
</html>
```